KAVLO ZenOS app needs a fun consumer interface design

KAVLO is a file transfer app aimed at consumers to help them get files onto their ZenOS devices. The app is based around each user having a personalised upload web address, and the ability to issue temporary time limited upload codes to friends and colleagues that they can use to send them files. The first version is already live in the widget shelf but we are working on a second, simplified version. You can see the screen shots for this on www.kavlo-example.com and I have attached a quick guide to app flow. The app now looks like a standard templated ZenOS 7 app. We need a design for the app that give it its own look, whilst retaining the standard ZenOS cues. It needs to look good on Palmo and Slabbo. We have a far east techno feel to the app at the moment with our characters, and we want to keep the logo. The website is currently a simple template, there's an ongoing competition to redesign that too - http://jobs.pitchmarket-example.com/job.aspx?id=813964
We have a working app with a reasonable design - we are looking for someone to take that design, add the polish a professional designer can bring, to make it pixel perfect and stand out as an app that has great design as well as great functionality.
We are also looking for something that works well on Palmo and Slabbo. See the attached screenshots of the Slabbo version - we want that version to look beautiful, not the big empty screen it is now.
Updates
Thanks for the designs so far, they look good. Could you draw them up for Slabbo size screens too please. The signup/login page and new code pages I think need the most attention as each page doesn't collect that much information, and so a lot of the screen is currently blank. I think we need some sort of background to set the content into for these pages.
(file 4 and file 6 are Slabbo screenshots)
The old app is installable for free from the Widget Shelf if that helps you get a feel for it on the Slabbo.
Target Market(s)
Consumers, techno savvy
Industry/Entity Type
Store
Font styles to use
Look and feel
Each slider illustrates characteristics of the customer's brand and the style your logo design should communicate.

```html
<!DOCTYPE html>
<html lang="en">
<head>
<meta charset="utf-8">
<title>KAVLO – Code Screen</title>
<link href="https://fonts.googleapis.com/css2?family=Roboto:wght@400;500&display=swap" rel="stylesheet">
<style>
  :root {
    --stage: #151515;
    --bar-blue: #2ba5e0;
    --button-blue: #1d8dc6;
    --button-edge: #16709f;
    --white: #ffffff;
    --ink-blue: #1b86c0;
    --screen-top: #efefef;
    --screen-mid: #e6e6e6;
    --screen-bottom: #e2e2e2;
    --figure-blue: #2a9ad6;
    --figure-tan: #d9ccb6;
    --strip-1: #b43e6c;
    --strip-2: #ee3f6e;
    --strip-3: #f47a31;
    --strip-4: #fdb946;
    --strip-5: #5dc1c4;
    --strip-6: #47a8a6;
    --strip-7: #9ecd40;
    --strip-8: #d3ea8e;
  }
  * { box-sizing: border-box; margin: 0; padding: 0; }
  html, body {
    width: 1200px;
    height: 2271px;
    overflow: hidden;
    background: var(--stage);
    font-family: "Roboto", Arial, sans-serif;
  }
  .app-screen {
    position: absolute;
    left: 0;
    top: 70px;
    width: 1200px;
    height: 2130px;
    overflow: hidden;
    background:
      radial-gradient(ellipse 600px 500px at 40% 30%, rgba(255,240,235,0.6), transparent 70%),
      radial-gradient(ellipse 500px 400px at 85% 20%, rgba(240,250,255,0.8), transparent 70%),
      linear-gradient(180deg, var(--screen-top), var(--screen-mid) 60%, var(--screen-bottom));
  }
  .status-bar {
    position: absolute;
    left: 0; top: 0;
    width: 100%; height: 72px;
    background: var(--bar-blue);
    color: var(--white);
    font-size: 40px;
    display: flex;
    align-items: center;
    padding: 0 22px;
  }
  .status-left { display: flex; align-items: center; gap: 16px; }
  .signal { display: flex; gap: 4px; }
  .signal span {
    width: 18px; height: 18px; border-radius: 50%;
    border: 2.5px solid var(--white);
  }
  .signal span.on { background: var(--white); }
  .status-time {
    position: absolute; left: 0; right: 0; text-align: center;
    font-weight: 500;
  }
  .status-right {
    margin-left: auto; display: flex; align-items: center; gap: 12px;
  }
  .nav-bar {
    position: absolute;
    left: 0; top: 72px;
    width: 100%; height: 173px;
    background: var(--bar-blue);
    box-shadow: 0 3px 6px rgba(0,0,0,0.12);
  }
  .nav-title {
    position: absolute; left: 0; right: 0; top: 0; bottom: 0;
    display: flex; align-items: center; justify-content: center;
    color: var(--white);
    font-size: 57px;
  }
  .nav-button {
    position: absolute;
    top: 46px;
    height: 106px;
    background: var(--button-blue);
    border-bottom: 6px solid var(--button-edge);
    border-radius: 4px;
    color: var(--white);
    display: flex; align-items: center; justify-content: center;
  }
  .nav-back { left: 20px; width: 112px; }
  .nav-done { left: 967px; width: 213px; font-size: 52px; }
  .character {
    position: absolute;
    left: 507px; top: 432px;
    width: 178px; height: 437px;
    border-radius: 80px 80px 30px 30px;
    background: linear-gradient(180deg, var(--figure-tan) 0%, var(--figure-blue) 32%, var(--figure-blue) 58%, #8a7a66 62%, #7a6a58 100%);
    opacity: 0.9;
  }
  .upload-message {
    position: absolute;
    left: 0; right: 0; top: 983px;
    text-align: center;
    color: var(--ink-blue);
    font-size: 54px;
    line-height: 72px;
  }
  .upload-code {
    position: absolute;
    left: 276px; top: 1410px;
    width: 639px; height: 112px;
    background: var(--white);
    border: 3px solid var(--ink-blue);
    border-radius: 14px;
    color: var(--ink-blue);
    font-size: 54px;
    font-weight: 500;
    display: flex; align-items: center; justify-content: center;
    letter-spacing: 1px;
  }
  .colour-strip {
    position: absolute;
    left: 0; bottom: 0;
    width: 100%; height: 92px;
    display: flex;
  }
  .colour-strip span { flex: 1; }
  .colour-strip span:nth-child(1) { background: var(--strip-1); }
  .colour-strip span:nth-child(2) { background: var(--strip-2); }
  .colour-strip span:nth-child(3) { background: var(--strip-3); }
  .colour-strip span:nth-child(4) { background: var(--strip-4); }
  .colour-strip span:nth-child(5) { background: var(--strip-5); }
  .colour-strip span:nth-child(6) { background: var(--strip-6); }
  .colour-strip span:nth-child(7) { background: var(--strip-7); }
  .colour-strip span:nth-child(8) { background: var(--strip-8); }
</style>
</head>
<body>
  <main class="app-screen">
    <div class="status-bar">
      <div class="status-left">
        <div class="signal"><span class="on"></span><span class="on"></span><span class="on"></span><span></span><span></span></div>
        <span class="carrier">Carrio</span>
        <svg width="44" height="32" viewBox="0 0 44 32" aria-hidden="true">
          <path d="M22 30 L14 21 A12 12 0 0 1 30 21 Z" fill="#fff"/>
          <path d="M7 14 A21 21 0 0 1 37 14" stroke="#fff" stroke-width="4" fill="none"/>
          <path d="M1 7 A30 30 0 0 1 43 7" stroke="#fff" stroke-width="4" fill="none"/>
        </svg>
      </div>
      <div class="status-time">4:21 PM</div>
      <div class="status-right">
        <span>100%</span>
        <svg width="70" height="32" viewBox="0 0 70 32" aria-hidden="true">
          <rect x="1.5" y="1.5" width="60" height="29" rx="4" fill="none" stroke="#fff" stroke-width="3"/>
          <rect x="6" y="6" width="51" height="20" rx="2" fill="#fff"/>
          <rect x="64" y="10" width="5" height="12" rx="1.5" fill="#fff"/>
        </svg>
      </div>
    </div>

    <header class="nav-bar">
      <div class="nav-button nav-back">
        <svg width="34" height="50" viewBox="0 0 34 50" aria-label="Back">
          <path d="M26 6 L8 25 L26 44" stroke="#fff" stroke-width="6" fill="none" stroke-linecap="round" stroke-linejoin="round"/>
        </svg>
      </div>
      <h1 class="nav-title" style="font-weight:400">Code Screen</h1>
      <div class="nav-button nav-done">Done</div>
    </header>

    <div class="character" role="img" aria-label="KAVLO mascot character in a blue top with headphones"></div>

    <p class="upload-message">
      Your new upload code is below.<br>
      To use the code go to<br>
      www.kavlo-example.com and<br>
      enter the code.
    </p>

    <div class="upload-code">YASIGRHB</div>

    <div class="colour-strip" aria-hidden="true">
      <span></span><span></span><span></span><span></span>
      <span></span><span></span><span></span><span></span>
    </div>
  </main>
</body>
</html>
```